Lebel for 500g Honey Jar

We want a design for a 500g honey bottle or Jar as shown in the attached image . All Requirement has been put in the attached brief document .
Also Logo and images have been uploaded . Feel free to play arround with the selected solor schemes .

Target Market(s)

Retail Market

Industry/Entity Type

FMCG

Colors
00AB8E
00BBA5
67D7C9
C6EFE9
E9F9F6
59FF00
82FF00
B8FF75
E3FFCB
F4FFEA
FFC000
F8CF3A
FAE287
FDF2CF
FEFAEE
F0912C
F2A743
F7CA91
FBE8D2
FDF5EE
EE7325
F08F49
F5BC92
FAE3D3
FDF4ED

Requirements
Must have
• The desing must contain the company Address, Logo , and Nutritional Facts
Nice to have
• Image of a honey Bee , see samples attahed

```html
<!DOCTYPE html>
<html lang="en">
<head>
<meta charset="utf-8">
<title>Meadowly Pure Honey – 500g Label</title>
<link href="https://fonts.googleapis.com/css2?family=Poppins:wght@400;600;700&family=Dancing+Script:wght@500&family=Fredoka:wght@700&display=swap" rel="stylesheet">
<style>
  :root {
    --bg-yellow: #FFC000;
    --bg-glow: #F8DA1A;
    --label-orange: #F0912C;
    --label-amber: #F2A743;
    --label-gold: #F8CF3A;
    --label-light: #FAE287;
    --ink-dark: #2E2A2A;
    --ink-brown: #7A3A10;
    --honey-yellow: #FFE64A;
    --honey-shade: #D98A12;
    --band-brown: rgba(122, 58, 16, 0.6);
    --text-cream: #FEFAEE;
    --leaf-green: #00AB8E;
    --bee-tone: rgba(255, 238, 140, 0.85);
  }
  * { box-sizing: border-box; margin: 0; padding: 0; }
  html, body { width: 1200px; height: 1200px; overflow: hidden; }
  body {
    background: radial-gradient(circle at 50% 50%, var(--bg-glow) 0%, var(--bg-yellow) 75%);
    font-family: "Poppins", sans-serif;
    position: relative;
  }
  .label {
    position: absolute;
    left: 300px;
    top: 90px;
    width: 600px;
    height: 1020px;
    border-radius: 30% 30% 50% 50% / 10% 10% 42% 42%;
    overflow: hidden;
    background: linear-gradient(160deg, var(--label-orange) 0%, var(--label-amber) 35%, var(--label-gold) 55%, var(--label-amber) 80%, var(--label-orange) 100%);
    box-shadow: 0 10px 40px rgba(160, 80, 0, 0.25);
  }
  .honeycomb-area {
    position: absolute;
    inset: 0;
    background:
      radial-gradient(ellipse at 30% 10%, rgba(250, 226, 135, 0.6) 0%, transparent 40%),
      radial-gradient(ellipse at 80% 65%, rgba(247, 202, 145, 0.5) 0%, transparent 45%),
      radial-gradient(ellipse at 45% 93%, rgba(250, 226, 135, 0.55) 0%, transparent 30%);
  }
  .bee {
    position: absolute;
    border-radius: 50%;
    background: radial-gradient(ellipse, var(--bee-tone) 0%, rgba(255, 238, 140, 0.35) 45%, rgba(255, 238, 140, 0) 72%);
  }
  .bee-large { left: 300px; top: 45px; width: 215px; height: 160px; }
  .bee-small { left: 30px; top: 400px; width: 115px; height: 85px; }

  .label-text {
    position: absolute;
    left: 0;
    width: 100%;
    text-align: center;
    line-height: 1;
  }
  .brand {
    top: 300px;
    display: flex;
    justify-content: center;
    align-items: center;
    gap: 10px;
    font-weight: 600;
    font-size: 54px;
    color: var(--ink-dark);
  }
  .brand-dot {
    width: 12px;
    height: 12px;
    border-radius: 50%;
    background: var(--leaf-green);
  }
  .product-pure {
    top: 410px;
    font-family: "Dancing Script", cursive;
    font-weight: 500;
    font-size: 60px;
    color: var(--ink-brown);
  }
  .product-name {
    top: 478px;
    font-family: "Fredoka", sans-serif;
    font-weight: 700;
    font-size: 150px;
    letter-spacing: 2px;
    color: var(--honey-yellow);
    text-shadow: 0 4px 0 var(--honey-shade), 0 8px 14px rgba(122, 58, 16, 0.35);
  }
  .claim-band {
    top: 680px;
    left: 50%;
    width: auto;
    transform: translateX(-50%);
    white-space: nowrap;
    padding: 3px 30px;
    background: var(--band-brown);
    color: var(--text-cream);
    font-size: 16px;
    letter-spacing: 3px;
  }
  .claims {
    top: 730px;
    list-style: none;
    color: var(--text-cream);
    font-weight: 700;
    font-size: 15px;
    line-height: 1.35;
  }
  .distributor {
    top: 815px;
    color: var(--text-cream);
    font-size: 17px;
    line-height: 1.35;
  }
  .net-weight {
    top: 918px;
    color: var(--text-cream);
    font-weight: 600;
    font-size: 26px;
  }
</style>
</head>
<body>
  <section class="label">
    <div class="honeycomb-area" role="img" aria-label="Honeycomb pattern in golden and amber tones"></div>
    <div class="bee bee-large" role="img" aria-label="Illustration of a honey bee in flight"></div>
    <div class="bee bee-small" role="img" aria-label="Small illustration of a honey bee"></div>

    <div class="label-text brand">
      <span class="brand-name">meadowly</span>
      <span class="brand-dot"></span>
    </div>
    <p class="label-text product-pure">Pure</p>
    <h1 class="label-text product-name">HONEY</h1>
    <p class="label-text claim-band">100% Pure &amp; Natural</p>
    <ul class="label-text claims">
      <li>Zero additive</li>
      <li>zero colouring</li>
      <li>zero preservative</li>
    </ul>
    <p class="label-text distributor">Packed &amp; Distributed by<br>Fieldgrove Farms Limited</p>
    <p class="label-text net-weight">500g</p>
  </section>
</body>
</html>
```